Basic Health & Safety Illustration Poster

Jollyhop Leisure, a nationwide entertainment and inflatable goods suppliers, requires a double sided information sheet for our customers to enable them to safely and successfully use our products. The poster will be sent to the customer by both email and paper copy and therefore a PDF format would be preferred. On side 1 of the poster, this will be called 'Safe Use or Safety Sheet' and I have attached a copy of our previous design (called customer safety sheet). This year we want the design to be more clear, more up to date and more professional - you may use your own graphics if you wish. The side 2 of the poster will be called 'Troubleshooting Guide' and I have attached a guide (called customer manual) for this also that is currently a 6 page document, but this must be condensed to 1 page of information and pictures. Again, you can use your own graphics if you wish or the attached graphics and we would like the overall design to compliment the design on the other page. On the troubleshooting page, we would like a small area assigned that can be written on in Ink, to say the following 'Your driver for today is ..................... and if you need to contact me, please call......................

Target Market(s)

Adults - appealing multi-language audiences at times so pictures are essential.

Industry/Entity Type

Entertainment

Requirements
Must have
• Both pictorials and editorial. Company Logo and contact information - can be taken from website www.jollyhopleisure.co.uk, further information can be taken from website where required. Ideally the colours used will compliment the company logo.
Nice to have
• Professional design, but colorful.

```html
<!DOCTYPE html>
<html lang="en">
<head>
<meta charset="utf-8">
<title>Trouble Shooting and Equipment Manual</title>
<link rel="stylesheet" href="https://fonts.googleapis.com/css2?family=Lobster&family=Nunito:wght@700;800&family=PT+Sans+Narrow:wght@400;700&family=Gochi+Hand&display=swap">
<style>
:root{
  --navy:#2b3585;
  --blue:#3e55a4;
  --yellow:#f6c519;
  --cyan:#1ea3dc;
  --magenta:#e5177e;
  --orange:#f07f1e;
  --note:#f6f0cf;
  --text:#2a2a2a;
  --grey:#e9e9ec;
}
*{margin:0;padding:0;box-sizing:border-box}
html,body{width:855px;height:1200px;overflow:hidden}
body{position:relative;background:linear-gradient(#fff 0,#fff 480px,#e6e6ea 560px,#f1f1f3 900px,#dcdce0 1200px);font-family:"PT Sans Narrow",sans-serif;color:var(--text)}
.abs{position:absolute}
.stripes{top:0;left:0}
.note{position:absolute;background:var(--note);box-shadow:2px 3px 6px rgba(0,0,0,.25);font-family:"Gochi Hand",cursive;color:var(--navy);font-size:19px;line-height:1.05;padding:14px 14px}
.note-driver{left:34px;top:70px;width:150px;height:108px;transform:rotate(-8deg)}
.note-contact{left:452px;top:8px;width:132px;height:120px;transform:rotate(-10deg)}
.note .dots{display:block;margin-top:12px;letter-spacing:1px}
.subtitle{left:178px;top:150px;font-family:"Nunito",sans-serif;font-weight:800;font-size:16px;line-height:1.15;color:var(--blue)}
.title{left:500px;top:108px;font-family:"Lobster",cursive;font-size:34px;line-height:.95;color:var(--navy);transform:rotate(-9deg);text-align:center;text-shadow:-2px -2px 0 #fff,2px -2px 0 #fff,-2px 2px 0 #fff,2px 2px 0 #fff,3px 4px 4px rgba(0,0,0,.35)}
.safety{left:32px;top:199px}
.safety h2{font-family:"Nunito",sans-serif;font-weight:800;font-size:14px;color:#333}
.safety p{font-size:13px;line-height:17px;color:#444}
.band{left:0;width:855px;background:var(--blue);color:#fff;text-align:center}
.band-start{top:257px;height:24px;font-family:"Nunito",sans-serif;font-weight:800;font-size:14px;line-height:24px;letter-spacing:.5px}
.steps{left:0;top:281px;width:855px;height:188px;display:flex;background:#ddd;gap:2px}
.step{flex:1;background:#fff;text-align:center;padding:8px 5px 0}
.step svg{display:block;margin:0 auto 6px}
.step p{font-size:11.4px;line-height:12px;color:var(--navy)}
.step b{font-weight:700}
.pic{position:absolute;border-radius:2px}
.section h3{position:absolute;font-family:"Nunito",sans-serif;font-weight:800;font-size:12.5px;color:#333}
.body{position:absolute;font-size:10.2px;line-height:12.3px;color:#333}
.body p{margin-bottom:6.5px}
.band-crowd{top:902px;height:88px;padding-top:6px;font-size:10.6px;line-height:13px}
.band-crowd h3{font-family:"Nunito",sans-serif;font-weight:700;font-size:14px;margin-bottom:1px}
.band-crowd p{padding:0 40px}
</style>
</head>
<body>

<svg class="abs stripes" width="855" height="125" viewBox="0 0 855 125" aria-hidden="true">
  <defs>
    <pattern id="stripe" width="198" height="125" patternUnits="userSpaceOnUse">
      <rect x="0" width="22" height="125" fill="#2b3585"/>
      <rect x="22" width="22" height="125" fill="#e5177e"/>
      <rect x="44" width="22" height="125" fill="#d9c9a8"/>
      <rect x="66" width="22" height="125" fill="#8a64a8"/>
      <rect x="88" width="22" height="125" fill="#d9222e"/>
      <rect x="110" width="22" height="125" fill="#b9a3cf"/>
      <rect x="132" width="22" height="125" fill="#1c5e9c"/>
      <rect x="154" width="22" height="125" fill="#c1307a"/>
      <rect x="176" width="22" height="125" fill="#5a3f8c"/>
    </pattern>
  </defs>
  <rect width="855" height="125" fill="url(#stripe)"/>
  <path d="M0 108 C200 70 500 62 855 80 L855 125 L0 125Z" fill="#fff"/>
  <path d="M0 108 C200 70 500 62 855 80" stroke="#c8c8d0" stroke-width="3" fill="none"/>
</svg>

<div class="note note-driver">Your driver for today is<span class="dots">......................</span></div>
<div class="note note-contact">and if you need to contact me, please call<span class="dots">.....................</span></div>

<div class="abs subtitle">Portable RCD Connection and/or<br>Resetting from Power Failure</div>
<div class="abs title">Trouble Shooting and<br>Equipment Manual</div>

<div class="abs safety">
  <h2>General Safety</h2>
  <p>•All extension leads and electrical cables should be fully unwound and loosely coiled prior to use</p>
  <p>•Check cables for kinks, splits, general wear or obvious signs of damage</p>
</div>

<div class="abs band band-start">GETTING STARTED</div>

<div class="abs steps">
  <div class="step">
    <svg width="68" height="68" viewBox="0 0 68 68" aria-hidden="true"><circle cx="34" cy="34" r="33" fill="var(--yellow)"/><rect x="14" y="30" width="22" height="9" rx="2" fill="#fff"/><circle cx="46" cy="34" r="7" fill="none" stroke="#fff" stroke-width="3"/><path d="M30 20h12l-4-4M42 20l-4 4" stroke="#fff" stroke-width="3" fill="none"/></svg>
    <p>First, connect the plug into an appropriate socket and switch the socket to ON</p>
  </div>
  <div class="step">
    <svg width="68" height="68" viewBox="0 0 68 68" aria-hidden="true"><circle cx="34" cy="34" r="33" fill="var(--cyan)"/><path d="M50 34a16 16 0 1 1-5-11.6" stroke="#fff" stroke-width="6" fill="none"/><path d="M40 16l9 6-9 6z" fill="#fff"/><text x="34" y="37" font-size="9" fill="#fff" text-anchor="middle" font-family="sans-serif">reset</text></svg>
    <p>Press the RESET button, usually found at the top of the RCD until the red light indicator is illuminated.</p>
  </div>
  <div class="step">
    <svg width="68" height="68" viewBox="0 0 68 68" aria-hidden="true"><circle cx="34" cy="34" r="33" fill="var(--magenta)"/><rect x="26" y="24" width="16" height="20" rx="3" fill="#fff"/><path d="M30 24v-8M38 24v-8M34 44v10M16 16l36 36" stroke="#fff" stroke-width="3"/></svg>
    <p>Connect the Ceeform (blue, round plug) connector into the extension lead or directly into the Blower</p>
  </div>
  <div class="step">
    <svg width="68" height="68" viewBox="0 0 68 68" aria-hidden="true"><circle cx="34" cy="34" r="33" fill="var(--orange)"/><rect x="22" y="14" width="20" height="38" rx="9" fill="#fff"/><path d="M42 36h6v16" stroke="#fff" stroke-width="3" fill="none"/></svg>
    <p>Connect the extension lead into the Blower (if required), your equipment should power up momentarily</p>
  </div>
  <div class="step">
    <svg width="68" height="68" viewBox="0 0 68 68" aria-hidden="true"><circle cx="34" cy="34" r="33" fill="var(--cyan)"/><circle cx="34" cy="34" r="22" fill="#9fd6ef"/><text x="34" y="39" font-size="13" fill="#333" text-anchor="middle" font-family="sans-serif" font-weight="700">Test</text><path d="M16 16l36 36M52 16l-36 36" stroke="#fff" stroke-width="4"/></svg>
    <p>Do not press the TEST button on the RCD, this is for internal testing only and away from site by our trained personnel</p>
  </div>
  <div class="step">
    <svg width="68" height="68" viewBox="0 0 68 68" aria-hidden="true"><circle cx="34" cy="34" r="33" fill="var(--magenta)"/><path d="M18 30a16 16 0 0 1 28-8M50 38a16 16 0 0 1-28 8" stroke="#fff" stroke-width="5" fill="none"/><path d="M42 14l8 9-11 2zM26 54l-8-9 11-2z" fill="#fff"/></svg>
    <p>To disconnect the equipment, repeat the above steps in reverse (unplug Blower, unplug extension, turn off power at wall and disconnect the portable RCD)</p>
  </div>
  <div class="step">
    <svg width="68" height="68" viewBox="0 0 68 68" aria-hidden="true"><circle cx="34" cy="34" r="33" fill="var(--yellow)"/><rect x="14" y="30" width="22" height="9" rx="2" fill="#fff"/><circle cx="46" cy="34" r="7" fill="none" stroke="#fff" stroke-width="3"/><path d="M42 20H30l4-4M30 20l4 4" stroke="#fff" stroke-width="3" fill="none"/></svg>
    <p>In case of an error, you will find a spare portable RCD in the blue box that can be found at the back of your inflatable equipment.</p>
  </div>
  <div class="step">
    <svg width="68" height="68" viewBox="0 0 68 68" aria-hidden="true"><circle cx="34" cy="34" r="33" fill="var(--orange)"/><path d="M22 16c3-2 6 0 8 5s-1 7-3 8c1 5 5 10 10 12 2-2 4-4 8-2s6 5 4 8c-3 5-9 5-15 1S19 37 17 29c-1-6 1-11 5-13z" fill="#fff"/></svg>
    <p>For further advice, please call our offices on <b>0871 555 0142</b></p>
  </div>
</div>

<section class="section">
  <div class="pic" style="left:20px;top:515px;width:172px;height:125px;background:linear-gradient(135deg,#e8c23a 0,#9aa1b0 45,#f2f2f6 60%,#cfd0d8 100%)" role="img" aria-label="Blower on with flap up and blower off with flap down diagram"></div>
  <h3 style="left:205px;top:492px">Loss of Inflation</h3>
  <div class="body" style="left:205px;top:515px;width:615px">
    <p>1. If the Blower is still on (if not, please refer to RCD resetting) then the obvious signs lead to air leakage.</p>
    <p>2. Firstly, we are going to check the Blower Tube (Air Inlet), usually situated at the rear of a Bouncy Castle and sometimes at the side of an Inflatable Game. This is a tube that connects the Blower to the Inflatable and keeps it inflated during use.</p>
    <p>3. This tube is secured to the Blower Funnel (outlet) by placing the tube over the Blower funnel and securing this with straps. Occasionally due to natural movement, this can become loose and will need to be secured.</p>
    <p>4. This is best achieved by disconnecting the Blower from the extension lead.</p>
    <p>5. Loosen the previously tied straps and pull the Blower tube back onto the Blower funnel as much as reasonably possible. Sometimes mounting the Blower can aid this.</p>
    <p>6. Secure the Blower tube using the straps provided and tie securely. The tighter the hold, the least amount of air will escape.</p>
    <p>7. After carrying this procedure out, reconnect the Blower to the extension lead and the Blower will power momentarily.</p>
    <p>8. Ensure that the Blower is in a correct, upright position at all times and that the Blower tube is not bent or kinked. The same principle as a garden hosepipe, kinks or bending will restrict the inward flow.</p>
  </div>
</section>

<section class="section">
  <div class="pic" style="left:20px;top:728px;width:172px;height:115px;background:linear-gradient(160deg,#0e3f6e,#2a8fcf 50%,#0b3558)" role="img" aria-label="Close-up of a zipped side panel on an inflatable with escaping air"></div>
  <h3 style="left:205px;top:713px">Loss of Inflation</h3>
  <div class="body" style="left:205px;top:736px;width:615px">
    <p>1. On many inflatables, removing the air quickly for pack down can be a difficult task. Many modern inflatables are constructed with several side panels on the outside of the inflatable, close to the bottom. These side panels consist of a industry grade zipper, concealed under a flap secured by Velcro.</p>
    <p>2. Over time, due to natural movement of the inflatable, these zippers can become loose and as the picture illustrates, air will escape quickly.</p>
    <p>3. If you are experiencing loss of inflation, check the inflatable for these panels on each side, at the rear and sometimes on the underneath front end of any inflatable slide.</p>
    <p>4. Open the flaps and secure any zippers that have become loose. Make sure after securing the zipper, you replace the flap ensuring the Velcro has contacted ensuring a secure fit.</p>
    <p>5. Also check for a secondary Blower tube at the rear of the inflatable. Sometimes, manufacturers will not install air outlet panels but install a second Blower tube to give the same effect. Secure this by folding in half, rolling into itself and secure this with the straps provided, the very same principle we saw before when re-connecting the Blower tube.</p>
  </div>
</section>

<div class="abs band band-crowd">
  <h3>Loss of Inflation</h3>
  <p>•An overcrowded or overweight Bouncy Castle or Inflatable can be the most common reason for loss of inflation.</p>
  <p>•Whilst there is no set limits, which is difficult to determine as each person is of different weight and size, a general guide is to ensure that the participants on the equipment, can bounce freely without contact. As a good guide, if the participants are bouncing and moving and still bumping, we would strongly suggest that the some of the participants are removed until the Bouncy Castle/Inflatable becomes available for further use.</p>
</div>

<section class="section">
  <div class="pic" style="left:30px;top:1002px;width:160px;height:170px;background:linear-gradient(#f3f3f5,#e2e2e6)" role="img" aria-label="Generator ignition switch diagram showing off, on, start and reset positions"></div>
  <h3 style="left:210px;top:1026px">Loss of Power to Generator/Petrol Blower</h3>
  <div class="body" style="left:210px;top:1048px;width:620px;font-size:10.8px;line-height:13.3px">
    <p>If the Petrol Blower or Generator switches off for no obvious reason, the first check should be the fuel levels. If the fuel levels are low in the tank, you will need to follow the re-fuelling procedure. This must be carried out with the equipment switched off, at this point you would of evacuated all users off the inflatable equipment for this period. Check that you have the correct fuel before refuelling and using a funnel, refuel the tank. You may now restart the Petrol Blower/Generator by turning the power switch to ON. Turn the lever or switch marked ‘Fuel’ to ON Turn the lever or switch marked ‘Choke’ to ON Pull the starter and leave the equipment running for a few minutes so that the engine warms up. Turn off the Choke. (If the engine is still warm, you may not need to apply the Choke for restart)</p>
  </div>
</section>

</body>
</html>
```